Unique Editable Recipe Cards

Create 10 unique editable recipe cards. Please look at Vorla and see what Editable Recipe cards are popular to get an idea of what Cards will sell. Search for "Editable Recipe Cards". The final images will need to be editable in Canva.

```html
<!DOCTYPE html>
<html lang="en">
<head>
<meta charset="utf-8">
<title>Pumpkin Soup Recipe Card</title>
<link href="https://fonts.googleapis.com/css2?family=Nothing+You+Could+Do&family=Noto+Serif:wght@400&family=Mulish:wght@400&display=swap" rel="stylesheet">
<style>
  :root {
    --page: #ffffff;
    --panel: #fdf0e0;
    --ink: #1c1c1c;
    --photo-light: #f4f5f7;
    --photo-warm: #e9b640;
  }
  * { margin: 0; padding: 0; box-sizing: border-box; }
  html, body { width: 851px; height: 1200px; overflow: hidden; background: var(--page); }
  .card { position: relative; width: 851px; height: 1200px; background: var(--page); color: var(--ink); font-family: "Mulish", sans-serif; }
  .hero { position: absolute; left: 26px; top: 0; width: 799px; height: 289px;
    background: radial-gradient(circle at 61% 52%, var(--photo-warm) 0, #f1c95e 14%, #f4f3f0 26%, var(--photo-light) 60%); }
  .side-panel { position: absolute; left: 26px; top: 289px; width: 364px; height: 911px; background: var(--panel); }
  .title { position: absolute; left: 96px; top: 308px; font-family: "Nothing You Could Do", cursive; font-size: 44px; line-height: 1; white-space: nowrap; }
  .title-rule { position: absolute; left: 87px; top: 390px; width: 255px; height: 2px; background: var(--ink); }
  .meta { position: absolute; top: 426px; display: flex; align-items: center; gap: 10px; font-size: 16px; }
  .meta svg { display: block; }
  .meta--servings { left: 80px; }
  .meta--time { left: 219px; }
  .section-heading { position: absolute; font-family: "Noto Serif", serif; font-weight: 400; font-size: 24px; letter-spacing: 0.3px; }
  .ingredients-heading { left: 76px; top: 523px; }
  .notes-heading { left: 76px; top: 993px; font-size: 22px; }
  .directions-heading { left: 438px; top: 335px; }
  .ingredients { position: absolute; left: 76px; top: 599px; list-style: none; font-size: 17px; line-height: 32.7px; }
  .notes-text { position: absolute; left: 76px; top: 1034px; width: 240px; font-size: 14px; line-height: 24.8px; }
  .directions { position: absolute; left: 438px; top: 416px; width: 370px; list-style: none; counter-reset: step; font-size: 17px; line-height: 29.5px; }
  .directions li { position: relative; padding-left: 17px; counter-increment: step; }
  .directions li::before { content: counter(step) "."; position: absolute; left: 0; }
</style>
</head>
<body>
<main class="card">
  <div class="hero" role="img" aria-label="Photo of a white bowl of creamy pumpkin soup topped with crispy bacon, cream and chives, with toasted bread slices on a white plate"></div>

  <aside class="side-panel"></aside>

  <h1 class="title">Pumpkin Soup</h1>
  <div class="title-rule"></div>

  <div class="meta meta--servings">
    <svg width="18" height="36" viewBox="0 0 18 36" fill="none" stroke="#1c1c1c" stroke-width="1.6">
      <path d="M2 2v9c0 2 1 3 2.5 3S7 13 7 11V2M4.5 2v9M4.5 14v19a1 1 0 0 0 2 0V14"/>
      <path d="M14 2c-2 2-3 6-3 11h2v20a1 1 0 0 0 2 0V2z"/>
    </svg>
    <span>2 servings</span>
  </div>
  <div class="meta meta--time">
    <svg width="28" height="28" viewBox="0 0 28 28" fill="none" stroke="#1c1c1c" stroke-width="2">
      <circle cx="14" cy="14" r="12"/>
      <path d="M14 7v7l5 4"/>
    </svg>
    <span>15 minutes</span>
  </div>

  <h2 class="section-heading ingredients-heading">INGREDIENTS</h2>
  <ul class="ingredients">
    <li>100 ml milk</li>
    <li>50 g butter</li>
    <li>3 eggs</li>
    <li>1 tbs cocoa</li>
    <li>2 tsp baking soda</li>
    <li>a pinch of salt</li>
    <li>3 eggs</li>
  </ul>

  <h2 class="section-heading notes-heading">NOTES</h2>
  <p class="notes-text">Nunc nulla velit, feugiat vitae ex quis, lobortis porta leo. Donec dictum lectus in ex accumsan sodales. Pellentesque habitant morbi tristique.</p>

  <h2 class="section-heading directions-heading">DIRECTIONS</h2>
  <ol class="directions">
    <li>Nunc nulla velit, feugiat vitae ex quis, lobortis porta leo.</li>
    <li>Donec dictum lectus in ex accumsan sodales. Pellentesque habitant morbi tristique.</li>
    <li>Nunc nulla velit, feugiat vitae ex quis, lobortis porta leo. Donec dictum lectus in lentesque habitant morbi tristique. Nunc nulla velit, feugiat vitae ex quis, lobortis porta leo. Donec dictum lectus in ex.</li>
    <li>Habitant morbi tristique.Nunc nulla velit, feugiat vitae ex quis, lobortis porta leo. Donec dictum lectu,</li>
    <li>Donec dictum lectus in ex accumsan sodales. Pellentesque habitant morbi tristique.</li>
    <li>Nunc nulla velit, feugiat vitae ex quis, lobortis porta leo. Donec dictum lectus lobortis porta leo.</li>
    <li>Donec dictum lectus in ex accumsan sodales. Pellentesque habitant morbi tristique</li>
  </ol>
</main>
</body>
</html>
```